Business Card Design

We would like a business card that utilizes our current logo and keeps with the same feel - elegant and organic. Our farm isn't about mass production, it's about excellence, education, beautiful events and flowers - people, culture, and community.

Target Market(s)

Patrons to our farm who are interested in weddings, events, or our flowers and vegetables.

Contact Information for Business Card

Name, address, cell email (Rosalind Hepworth, 2718 Wintervale Rd, Longmont, CO 80517, cell 30.412.6387, email rosalind@wintervalefarm.example)

```html
<!DOCTYPE html>
<html lang="en">
<head>
<meta charset="UTF-8">
<title>Wintervale Farm – Business Card</title>
<link href="https://fonts.googleapis.com/css2?family=Montserrat:wght@400;500&family=Allura&display=swap" rel="stylesheet">
<style>
  :root {
    --backdrop: #161616;
    --card: #2b2b2b;
    --card-back: #262626;
    --sage: #7d9580;
    --copper: #b07f53;
    --ink-light: #f1f1ef;
    --muted: #3d3d3d;
    --divider: #5a5a5a;
  }
  * { margin: 0; padding: 0; box-sizing: border-box; }
  html, body {
    width: 1200px; height: 900px; overflow: hidden;
    background: var(--backdrop);
    font-family: "Montserrat", Arial, sans-serif;
  }
  .sheet {
    width: 1200px; height: 900px;
    display: flex; flex-direction: column;
    align-items: center; justify-content: center; gap: 34px;
  }
  .card {
    position: relative;
    width: 700px; height: 400px;
    background: var(--card);
    box-shadow: 0 12px 30px rgba(0,0,0,.45);
    overflow: hidden;
  }
  .card--back { background: var(--card-back); }

  .brand {
    position: absolute;
    display: flex; align-items: center; gap: 12px;
    color: var(--sage);
    font-weight: 500;
    letter-spacing: .18em;
    text-transform: uppercase;
    white-space: nowrap;
  }
  .brand__dot { border-radius: 50%; background: currentColor; flex: none; }
  .card--front .brand { top: 70px; right: 56px; font-size: 22px; }
  .card--front .brand__dot { width: 13px; height: 13px; }
  .card--back .brand {
    top: 50%; left: 50%; transform: translate(-50%, -50%);
    font-size: 40px; color: var(--muted);
  }
  .card--back .brand__dot { width: 22px; height: 22px; }

  .person {
    position: absolute; top: 178px; left: 16px; width: 302px;
    text-align: right;
  }
  .person__name {
    font-family: "Allura", cursive;
    font-size: 42px; line-height: 1;
    color: var(--sage);
    white-space: nowrap;
  }
  .person__role {
    margin-top: 10px;
    font-size: 15px; color: var(--ink-light);
  }

  .divider {
    position: absolute; left: 334px; top: 184px;
    width: 1px; height: 96px; background: var(--divider);
  }

  .contacts {
    position: absolute; left: 356px; top: 190px;
    list-style: none;
    display: flex; flex-direction: column; gap: 13px;
  }
  .contacts__item {
    display: flex; align-items: center; gap: 10px;
    font-size: 15px; color: var(--ink-light);
    white-space: nowrap;
  }
  .contacts__icon { width: 14px; height: 14px; fill: var(--copper); flex: none; }

  .address {
    position: absolute; left: 56px; top: 320px;
    font-size: 15px; color: var(--ink-light);
    white-space: nowrap;
  }

  .band {
    position: absolute; left: 0; right: 0; bottom: 0;
    height: 20px; background: var(--sage);
  }
</style>
</head>
<body>
<main class="sheet">
  <section class="card card--front" aria-label="Business card front">
    <div class="brand"><span class="brand__dot"></span>Wintervale Farm</div>

    <div class="person">
      <p class="person__name">Theodore Ashcombe</p>
      <p class="person__role">Director/Founder</p>
    </div>

    <div class="divider"></div>

    <ul class="contacts">
      <li class="contacts__item">
        <svg class="contacts__icon" viewBox="0 0 24 24" aria-hidden="true"><path d="M6.6 10.8a15.1 15.1 0 0 0 6.6 6.6l2.2-2.2a1 1 0 0 1 1-.25 11.4 11.4 0 0 0 3.6.57 1 1 0 0 1 1 1V20a1 1 0 0 1-1 1A17 17 0 0 1 3 4a1 1 0 0 1 1-1h3.5a1 1 0 0 1 1 1c0 1.250.2 2.450.57 3.6a1 1 0 0 1-.25 1z"/></svg>
        30.412.6387
      </li>
      <li class="contacts__item">
        <svg class="contacts__icon" viewBox="0 0 24 24" aria-hidden="true"><path d="M2 5h20v14H2z"/><path d="M2 5l10 8 10-8" fill="none" stroke="var(--card)" stroke-width="1.6"/></svg>
        rosalind@wintervalefarm.example
      </li>
      <li class="contacts__item">
        <svg class="contacts__icon" viewBox="0 0 24 24" aria-hidden="true"><circle cx="12" cy="12" r="10"/><path d="M2 12h20M12 2c3 3 3 17 0 20M12 2c-3 3-3 17 0 20" fill="none" stroke="var(--card)" stroke-width="1.4"/></svg>
        www.wintervalefarm.example
      </li>
    </ul>

    <p class="address">Rosalind Hepworth, 2718 Wintervale Rd, Longmont, CO 80517</p>

    <div class="band"></div>
  </section>

  <section class="card card--back" aria-label="Business card back">
    <div class="brand"><span class="brand__dot"></span>Wintervale Farm</div>
  </section>
</main>
</body>
</html>
```